Q.B.Y 'Qafilat Bin Yusr' for General Transportation

this company is a Iraqi based company.
It provides a number of logistics activities such as;
Overland Transportation
High and heavy logistics
Customs clearance
warehousing
Automotive logistics
The company has been registered since 2009.
If you have any other questions please feel free to ask.
Target Market(s)
Automotive
White goods
All Trading sectors
Industry/Entity Type
Automotive

```html
<!DOCTYPE html>
<html lang="en">
<head>
<meta charset="utf-8">
<title>Qafilat Bin Yusr Transportation</title>
<link rel="stylesheet" href="https://fonts.googleapis.com/css2?family=Jura:wght@400;700&family=Exo+2:ital,wght@1,800&family=Jost:wght@400&family=Arimo:wght@400;700&display=swap">
<style>
  :root{
    --navy:#0c2d63;
    --navy-dark:#0a2350;
    --nav-bg:#2e2e2e;
    --page:#ffffff;
    --band:#ebebeb;
    --text:#222222;
    --muted:#8a8a8a;
    --orange:#f28a0c;
    --footer:#333333;
    --footer-deep:#222222;
    --tab1:#3d3d3d;
    --tab2:#555555;
    --tab3:#6a6a6a;
  }
  *{box-sizing:border-box;margin:0;padding:0}
  html,body{width:946px;height:1200px;overflow:hidden}
  body{position:relative;background:var(--page);font-family:"Arimo",Arial,sans-serif;color:var(--text)}
  .abs{position:absolute}

  .main-nav{left:0;top:0;width:946px;height:35px;background:var(--nav-bg)}
  .main-nav a{position:absolute;top:0;height:35px;line-height:35px;color:#fff;font-size:12px;text-decoration:none;transform:translateX(-50%);white-space:nowrap}
  .main-nav a.is-active{top:4px;height:26px;line-height:26px;padding:0 16px;background:#1d1d1d;border:1px solid #555;border-radius:3px}

  .brand{left:82px;top:62px;display:flex;align-items:center;gap:12px}
  .brand-mark{width:48px;height:48px;background:var(--navy)}
  .brand-text{font-family:"Jura",sans-serif;color:var(--navy);line-height:1.15}
  .brand-name{font-size:17px;font-weight:700}
  .brand-sub{font-size:15px}
  .brand-url{font-size:11px}

  .support{left:636px;top:68px;display:flex;gap:12px;align-items:flex-start}
  .support-text{font-family:"Jost",sans-serif;font-size:13.5px;color:#222;line-height:20px}
  .support-text b{color:var(--navy);font-weight:400}

  .hero{left:82px;top:133px;width:783px;height:298px}
  .sector-tab{position:absolute;top:0;width:31px;height:298px;color:#fff;font-size:15px;letter-spacing:1px}
  .sector-tab span{position:absolute;left:6px;top:38px;writing-mode:vertical-rl}
  .sector-tab i{position:absolute;left:8px;bottom:9px;width:15px;height:15px;border-radius:50%;background:#9a9a9a}
  .hero-panel{position:absolute;left:93px;top:0;width:244px;height:298px;background:var(--navy);color:#fff;padding:32px 14px 0 15px}
  .hero-panel h2{font-family:"Jura",sans-serif;font-weight:400;font-size:26px;line-height:30px}
  .hero-panel h2 strong{display:block;font-weight:700;font-size:26px;letter-spacing:.5px}
  .hero-panel p{margin-top:12px;font-size:10.3px;line-height:14px;padding-left:3px}
  .read-more{display:inline-block;margin:14px 0 0 3px;padding:2px 6px;background:#fff;color:#222;border-radius:9px;font-size:8px}
  .slide-no{position:absolute;left:211px;top:270px;width:16px;height:16px;border-radius:50%;background:#bbb;color:#fff;font-size:9px;text-align:center;line-height:16px}
  .hero-photo{position:absolute;left:338px;top:0;width:445px;height:298px;background:linear-gradient(180deg,#d4d6d8 0%,#c6c2ba 45%,#a8a39a 100%)}

  .content-band{left:0;top:431px;width:946px;height:555px;background:var(--band)}

  .why-title{left:80px;top:469px;font-family:"Exo 2",sans-serif;font-style:italic;font-weight:800;font-size:22px;color:var(--navy)}
  .why-photo{left:81px;top:515px;width:149px;height:151px;background:linear-gradient(160deg,#3b3a36,#7a5a30 50%,#2b2a28)}
  .why-copy{left:240px;top:513px;width:366px;font-size:9.7px;line-height:15.8px;color:#222}
  .why-copy p+p{margin-top:15.8px}

  .quote-form{left:622px;top:469px;width:244px;height:237px;background:var(--navy);border-radius:3px;padding:9px 0 0 24px}
  .quote-form h3{font-family:"Jura",sans-serif;font-weight:400;font-size:19px;color:#fff;letter-spacing:.5px}
  .field{display:block;width:198px;height:21px;margin-top:10px;background:#fff;border-radius:3px;font-size:9.5px;color:#555;line-height:21px;padding-left:7px;position:relative}
  .field:first-of-type{margin-top:13px}
  .field svg{position:absolute;right:6px;top:8px}
  .submit{position:absolute;left:152px;top:204px;width:70px;height:21px;background:var(--orange);color:#fff;font-weight:700;font-size:12.5px;text-align:center;line-height:21px;border-radius:2px}

  .divider{left:81px;top:734px;width:784px;height:1px;background:#cfcfcf}

  .sector-card{width:222px;height:178px;background:#fff;border-radius:6px;text-align:center;box-shadow:0 1px 3px rgba(0,0,0,.12)}
  .sector-card .photo{margin:16px auto 0;width:187px;height:76px}
  .sector-card h4{font-family:"Jost",sans-serif;font-weight:400;font-size:14.5px;color:var(--navy);margin-top:9px;letter-spacing:.3px}
  .sector-card p{font-size:9.6px;line-height:14px;color:#333;padding:0 8px}
  .card-tab{position:absolute;left:86px;top:172px}

  .testimonials-band{left:0;top:986px;width:946px;height:167px;background:var(--footer)}
  .testimonials h3{font-family:"Jost",sans-serif;font-weight:400;font-size:16px;color:#fff}
  .testimonials p{margin-top:6px;width:410px;font-size:9.4px;line-height:12.8px;color:#6a6a6a}
  .testimonials cite{display:block;text-align:right;width:386px;font-style:normal;color:#fff;font-size:9.4px;margin-top:1px}

  .newsletter{left:658px;top:1005px;width:197px;height:113px;background:#2b2b2b;border-radius:3px;padding:22px 0 0 11px}
  .newsletter h3{font-family:"Jost",sans-serif;font-weight:400;font-size:16px;color:#fff}
  .newsletter .input{margin-top:8px;width:172px;height:17px;background:#fff;border:2px solid #ccc}
  .newsletter .unsub{position:absolute;left:14px;top:81px;font-size:9.5px;color:#aaa;text-decoration:underline}
  .newsletter .btn{position:absolute;left:122px;top:72px;width:61px;height:19px;background:#151515;color:#fff;font-size:9.5px;text-align:center;line-height:19px;border-radius:2px}

  .legal-bar{left:0;top:1153px;width:946px;height:47px;background:var(--footer-deep);text-align:center;color:#999;font-size:9.6px;line-height:16px;padding-top:11px}
</style>
</head>
<body>

<nav class="main-nav abs">
  <a class="is-active" style="left:118px">Home</a>
  <a style="left:210px">About QBY</a>
  <a style="left:311px">Services</a>
  <a style="left:405px">For Sale</a>
  <a style="left:499px">About Us</a>
  <a style="left:598px">Jay Videos</a>
  <a style="left:715px">News &amp; Events</a>
  <a style="left:837px">Contact Us</a>
</nav>

<header>
  <div class="brand abs">
    <div class="brand-mark"></div>
    <div class="brand-text">
      <div class="brand-name">Qafilat Bin Yusr</div>
      <div class="brand-sub">Transportation</div>
      <div class="brand-url">www.qbytrans.com</div>
    </div>
  </div>
  <div class="support abs">
    <svg width="28" height="28" viewBox="0 0 28 28" aria-hidden="true">
      <circle cx="14" cy="14" r="10" fill="none" stroke="#9a9a9a" stroke-width="3" stroke-dasharray="4 2"/>
      <circle cx="14" cy="14" r="6" fill="none" stroke="#cfcfcf" stroke-width="2"/>
    </svg>
    <div class="support-text">Your 24/7 <b>Support Partner:</b><br>+6123457700</div>
  </div>
</header>

<section class="hero abs">
  <div class="sector-tab" style="left:0;background:var(--tab1)"><span>All Trading sectors</span><i></i></div>
  <div class="sector-tab" style="left:31px;background:var(--tab2)"><span>White goods</span><i></i></div>
  <div class="sector-tab" style="left:62px;background:var(--tab3)"><span>Automotive</span><i></i></div>
  <div class="hero-panel">
    <h2>Overland <strong>Transportation</strong></h2>
    <p>simply dummy text of the printing and type-setting industry. Lorem Ipsum has been the industry's standard dummy text ever since the 1500s,</p>
    <span class="read-more">READ MORE</span>
    <span class="slide-no">01</span>
  </div>
  <div class="hero-photo" role="img" aria-label="Crane loading an orange heavy trailer onto a flatbed truck at a depot"></div>
</section>

<div class="content-band abs"></div>

<h2 class="why-title abs">WHY CHOOSE QBY ?</h2>
<div class="why-photo abs" role="img" aria-label="Orange drilling rig working in a mine tunnel"></div>
<div class="why-copy abs">
  <p>Lorem ipsum dolor sit amet, consectetur adipiscing elit. Quisque dapibus accumsan orci, pretium eleifend arcu adipiscing eget. Fusce accumsan facilisis tincidunt. Phasellus tempor enim purus, vitae venenatis est. Ut imperdiet hendrerit pulvinar. Cras at tellus a enim condimentum mollis ut et tellus. Mauris dolor magna, elementum eu dictum eu, fermentum a nibh. Praesent ut dui lectus, vel lacinia sem.</p>
  <p>Praesent commodo malesuada urna, quis convallis risus dictum et. Nunc enim purus, vitae venenatis est. Ut imperdiet hendrerit pulvinar. Cras at tellus adapibus interdum libero, et semper eros auctor ac.</p>
</div>

<form class="quote-form abs">
  <h3>Request a Quote</h3>
  <span class="field">Name*</span>
  <span class="field">Contact Number*</span>
  <span class="field">Email</span>
  <span class="field">Reg No*</span>
  <span class="field">Type Of Remap<svg width="9" height="5" viewBox="0 0 9 5"><path d="M0 0h9L4.5 5z" fill="#555"/></svg></span>
  <span class="submit">Submit</span>
</form>

<div class="divider abs"></div>

<article class="sector-card abs" style="left:87px;top:753px">
  <div class="photo" role="img" aria-label="Car assembly line with workers" style="background:linear-gradient(180deg,#6f7c8c,#8d99a8 50%,#3d4756)"></div>
  <h4>AUTOMOTIVE</h4>
  <p>Vestibulum rutrum pharetra diam, eget dapi-bus leo vehicula ut. Fusce aliquam, odio eget adipiscing lobortis.</p>
  <svg class="card-tab" width="50" height="20" viewBox="0 0 50 20" aria-hidden="true"><path d="M0 0h50Q40 20 25 20T0 0z" fill="#fff"/><path d="M15 5h20l-10 8z" fill="#333"/></svg>
</article>

<article class="sector-card abs" style="left:358px;top:755px">
  <div class="photo" role="img" aria-label="Technician unloading appliances beside a blue delivery van" style="margin-top:21px;background:linear-gradient(90deg,#8a8f96,#c6c9cc 40%,#2f6f98)"></div>
  <h4>WHITE GOODS</h4>
  <p>Vestibulum rutrum pharetra diam, eget dapi-bus leo vehicula ut. Fusce aliquam, odio eget adipiscing lobortis.</p>
  <svg class="card-tab" width="50" height="20" viewBox="0 0 50 20" aria-hidden="true"><path d="M0 0h50Q40 20 25 20T0 0z" fill="#fff"/><path d="M15 5h20l-10 8z" fill="#333"/></svg>
</article>

<article class="sector-card abs" style="left:634px;top:756px">
  <div class="photo" role="img" aria-label="Forklift moving pallets in a container yard" style="margin-top:21px;background:linear-gradient(180deg,#8fa6c0,#5478a4 45%,#a48464)"></div>
  <h4>ALL TRADING SECTORS</h4>
  <p>Vestibulum rutrum pharetra diam, eget dapi-bus leo vehicula ut. Fusce aliquam, odio eget adipiscing lobortis.</p>
  <svg class="card-tab" width="50" height="20" viewBox="0 0 50 20" aria-hidden="true"><path d="M0 0h50Q40 20 25 20T0 0z" fill="#fff"/><path d="M15 5h20l-10 8z" fill="#333"/></svg>
</article>

<footer>
  <div class="testimonials-band abs"></div>
  <div class="testimonials abs" style="left:78px;top:1007px">
    <h3>Testimonials</h3>
    <p>The representative I spoke with verified my info and said he would call me back once he looked into the problem. Sure enough he called back within 10 minutes and pointed the problem out to me (duplex setting on my end). Once I made the change the line immediately performed as expected. From the moment I first contacted you regarding our need for connectivity, this has been without a doubt my best experience with any ISP I have worked with around the world. Thanks to you guys 2007 will be a cheaper and more productive year for us at NETORA.</p>
    <cite>Daniel Reyes</cite>
  </div>
  <div class="newsletter abs">
    <h3>Newsletter</h3>
    <div class="input"></div>
    <span class="unsub">Unsubscribe</span>
    <span class="btn">subscribe</span>
  </div>
  <div class="legal-bar abs">
    This website was developed by Qafilat Bin Yusr Transportation. provider of Software Development Solutions<br>
    QBY integration and LinkSure Automation development.
  </div>
</footer>

</body>
</html>
```